Conference for Teenagers Needs Event Graphics

I am in need of event graphics for our upcoming event. This event, titled "Maple Ridge Youth Conference", is a weekend event for teenagers 11-19 years old. They hear from speakers, listen to a band, and do other fun activities. Our theme is "Together." Graphic design should have a young adult/older teen feel. Clean, not very bright colors.

Event Info:
November 6-8, 2020
Velmora Exhibit Hall, Sioux Falls, SD
Speakers: TBD (will give name and picture before final approval)
Worship: (band name TBD before final approval)
MapleRidgeYC-event.com
#872MR
Our Organization Logo (attached): PA Crestway

Once designed, I need the following graphics file sizes:
-11x17 Vertical Poster design: include all event info AND a "blank" spot/box for groups to add their own details/information. Also include the KRV logo and our organization logo PA Crestway in someway.
-4x3 horizontal postcard: include all event info on 1 side including PACrestway logo and KRV; blank backside
-Main Graphic Slide: formatted to fit a widescreen 16x9 screen. Include event name, hashtag, KRV and PA Crestway logo
-social media graphics for event: can incorporate some or all of the event details
-4.25x 2.75 vertical badge: include event title on front with PA Crestway logo

Target Market(s)

Young adults or older teenagers

Requirements
Must have
• -event info
-PA Crestway Logo & KRV logo

```html
<!DOCTYPE html>
<html lang="en">
<head>
<meta charset="utf-8">
<title>Maple Ridge Youth Conference – Event Graphics</title>
<link rel="stylesheet" href="https://fonts.googleapis.com/css2?family=Amatic+SC:wght@700&family=Caveat:wght@500&family=Montserrat:wght@500&display=swap">
<style>
  :root {
    --page-bg: #eff3f6;
    --label: #2a4a6b;
    --navy-top: #1f5b88;
    --navy-bottom: #2b3762;
    --orange-top: #df8b5d;
    --orange-bottom: #ea5743;
    --sky-light: #5fcdf2;
    --sky: #2aa6dc;
    --sky-deep: #1796cf;
    --lettering: #e4e6e8;
    --coral: #e77b55;
    --white: #ffffff;
  }
  * { margin: 0; padding: 0; box-sizing: border-box; }
  html, body { width: 1200px; height: 1000px; overflow: hidden; }
  body {
    position: relative;
    background: var(--page-bg);
    font-family: "Amatic SC", "Patrick Hand", cursive;
    color: var(--white);
  }
  .piece { position: absolute; overflow: hidden; box-shadow: 0 4px 18px rgba(30, 50, 80, 0.12); }
  .piece-label {
    position: absolute;
    font-family: "Montserrat", Arial, sans-serif;
    font-weight: 500;
    font-size: 17px;
    color: var(--label);
  }
  .org-mark, .partner-mark {
    position: absolute;
    display: flex;
    align-items: center;
    gap: 5px;
    font-weight: 700;
    text-transform: uppercase;
    color: var(--white);
    white-space: nowrap;
    line-height: 1;
  }
  .org-mark .dot { display: block; background: var(--white); border-radius: 50%; }
  .sticker {
    position: absolute;
    border-radius: 50%;
    background: radial-gradient(circle at 40% 35%, var(--sky-light), var(--sky) 60%, var(--sky-deep));
    box-shadow: 0 8px 22px rgba(0, 0, 0, 0.28);
  }

  /* Theme title */
  .theme {
    position: absolute;
    line-height: 1;
    white-space: nowrap;
    transform: translate(-50%, -50%) rotate(-6deg);
    text-align: center;
  }
  .theme-title {
    display: block;
    font-family: "Caveat", "Dancing Script", cursive;
    font-weight: 500;
    color: var(--lettering);
  }
  .theme-tag {
    display: block;
    font-family: "Amatic SC", cursive;
    font-weight: 700;
    color: var(--coral);
    text-align: right;
  }

  .event-info { position: absolute; line-height: 1; white-space: nowrap; text-transform: uppercase; }
  .event-info p { margin: 0; }
  .web-line { display: flex; align-items: center; }
  .web-line::before, .web-line::after {
    content: ""; display: block; height: 1px; background: var(--white);
  }

  /* Poster */
  .poster {
    left: 102px; top: 67px; width: 544px; height: 840px;
    background: linear-gradient(180deg, var(--navy-top), var(--navy-bottom));
  }
  .poster .org-mark { right: 38px; top: 44px; font-size: 24px; }
  .poster .org-mark .dot { width: 12px; height: 12px; }
  .poster .sticker { left: 60px; top: 180px; width: 426px; height: 426px; }
  .poster .theme { left: 188px; top: 210px; }
  .poster .theme-title { font-size: 104px; }
  .poster .theme-tag { font-size: 42px; margin-top: -22px; margin-right: -20px; }
  .poster .event-info { left: 173px; top: 638px; }
  .poster .date { font-size: 28px; }
  .poster .venue { font-size: 14px; margin-top: 9px; }
  .poster .speakers { font-size: 22px; margin-top: 8px; }
  .poster .worship { font-size: 28px; margin-top: 6px; }
  .poster .web-line { font-size: 14px; margin-top: 26px; gap: 8px; margin-left: 4px; }
  .poster .web-line::before, .poster .web-line::after { width: 28px; }

  /* Postcard */
  .postcard {
    left: 691px; top: 67px; width: 411px; height: 289px;
    background: linear-gradient(200deg, var(--orange-top), var(--orange-bottom));
  }
  .postcard .sticker { left: 34px; top: 60px; width: 186px; height: 186px; }
  .postcard .theme { left: 88px; top: 90px; }
  .postcard .theme-title { font-size: 46px; }
  .postcard .theme-tag { font-size: 19px; margin-top: -10px; margin-right: -8px; }
  .postcard .event-info { left: 246px; top: 104px; }
  .postcard .date { font-size: 17px; }
  .postcard .venue { font-size: 8px; margin-top: 5px; }
  .postcard .speakers { font-size: 13px; margin-top: 5px; }
  .postcard .worship { font-size: 17px; margin-top: 4px; }
  .postcard .web-line { font-size: 8px; margin-top: 15px; gap: 5px; }
  .postcard .web-line::before, .postcard .web-line::after { width: 16px; }
  .postcard .partner-mark { left: 248px; top: 241px; font-size: 20px; }
  .postcard .org-mark { left: 300px; top: 243px; font-size: 15px; }
  .postcard .org-mark .dot { width: 7px; height: 7px; }

  /* Badge */
  .badge {
    left: 815px; top: 538px; width: 178px; height: 322px;
    border-radius: 12px;
    background: linear-gradient(180deg, var(--sky-light), var(--sky-deep));
  }
  .badge .org-mark { right: 14px; top: 40px; font-size: 12px; }
  .badge .org-mark .dot { width: 6px; height: 6px; }
  .badge .theme { left: 88px; top: 172px; transform: translate(-50%, -50%); }
  .badge .theme-title { font-size: 46px; color: var(--white); }
  .badge .theme-tag { font-size: 18px; margin-top: -10px; margin-right: -6px; }
</style>
</head>
<body>

  <section class="piece poster" aria-label="Poster">
    <div class="org-mark"><span class="dot"></span>PA Crestway</div>
    <div class="sticker">
      <h1 class="theme"><span class="theme-title">together</span><span class="theme-tag">#872MR</span></h1>
    </div>
    <div class="event-info">
      <p class="date">November 6-8, 2020</p>
      <p class="venue">Velmora Exhibit Hall, Sioux Falls, SD</p>
      <p class="speakers">Speakers: Name Lastname</p>
      <p class="worship">Worship: Band Name</p>
      <p class="web-line">MapleRidgeYC-event.com</p>
    </div>
  </section>
  <p class="piece-label" style="left:102px; top:928px;">Poster</p>

  <section class="piece postcard" aria-label="Postcard">
    <div class="sticker">
      <h2 class="theme"><span class="theme-title">together</span><span class="theme-tag">#872MR</span></h2>
    </div>
    <div class="event-info">
      <p class="date">November 6-8, 2020</p>
      <p class="venue">Velmora Exhibit Hall, Sioux Falls, SD</p>
      <p class="speakers">Speakers: Name Lastname</p>
      <p class="worship">Worship: Band Name</p>
      <p class="web-line">MapleRidgeYC-event.com</p>
    </div>
    <div class="partner-mark">KRV</div>
    <div class="org-mark"><span class="dot"></span>PA Crestway</div>
  </section>
  <p class="piece-label" style="left:691px; top:383px;">Postcard</p>

  <section class="piece badge" aria-label="Badge">
    <div class="org-mark"><span class="dot"></span>PA Crestway</div>
    <h2 class="theme"><span class="theme-title">together</span><span class="theme-tag">#872MR</span></h2>
  </section>
  <p class="piece-label" style="left:689px; top:928px;">Badge</p>

</body>
</html>
```